Hunting club needs a new web design !

We need a new web design for our hunting club located in Poland, called "ZAWIRA". The club was founded in 1945. Colors that we would like to see in the project are the colors of the forest. The website should be built in such a way that all text elements can be changed to another language and can't be graphic.
"ZAWIRA" means - big, thick forest in which the game, small and big resides

Target Market(s)

hunters,

Industry/Entity Type

Hunting

Coding

Coded - Design and coding required

Number of Pages Required

5+ page

Font styles to use
Decorative

Colors

Designer to choose colors to be used in the design.

Requirements
Must have
• current date, calendar,
• must contain almost all materials from our current web page
• http://zawira-dolnomokra.webnika.pl/
• new web address: zawiradmk.pl
Nice to have
• current weather in three hunting regions that we allowed to hunt, or indicated by the visitor on the map placed on our web,
• actual phase of the moon, actual moon rising hour, actual moon set hour, actual sun rise hour, actual sun set hour, current weather in region (stalowa wola, poland)
• wood, forest, deers, boars,
Should not have
• mountain photos, modern look, white or bright backgrounds,

```html
<!DOCTYPE html>
<html lang="en">
<head>
<meta charset="utf-8">
<title>ZAWIRA – Hunting Club</title>
<link href="https://fonts.googleapis.com/css2?family=Montserrat:wght@400;600;700&family=Open+Sans:wght@400;600;700&family=Raleway:wght@400;500&display=swap" rel="stylesheet">
<style>
:root{
  --green:#4f9a0c;
  --green-light:#63b117;
  --olive:#4a4513;
  --olive-dark:#3d3c1a;
  --title-olive:#4d4a10;
  --navy:#0d1836;
  --box-top:#3a69b0;
  --box-bottom:#1d4f96;
  --text:#333;
  --muted:#666;
  --white:#fff;
}
*{margin:0;padding:0;box-sizing:border-box}
html,body{width:1200px;height:3000px;overflow:hidden;background:var(--white)}
body{position:relative;font-family:"Open Sans",sans-serif;color:var(--text)}
.abs{position:absolute}
.head{font-family:"Montserrat",sans-serif}

/* header */
.brand{left:100px;top:22px;display:flex;align-items:center;gap:10px;font-family:"Open Sans",sans-serif;font-weight:700;font-size:34px;color:var(--green-light)}
.brand .dot{width:22px;height:22px;border-radius:50%;background:var(--green-light)}
.main-nav{top:50px;font-size:15px;font-weight:600;color:#222}
.sub-nav{left:0;top:124px;width:1200px;height:62px;background:var(--olive);border-top:3px solid #6b6420;border-bottom:3px solid #6b6420}
.sub-nav span{position:absolute;top:18px;font-size:14px;font-weight:600;color:var(--white)}

/* hero */
.hero{left:0;top:186px;width:1200px;height:400px;background:linear-gradient(180deg,#3f4b2c 0%,#5d6d3a 35%,#7f9546 60%,#4a5a26 100%)}
.hero-title{left:0;top:306px;width:1200px;text-align:center;font-family:"Montserrat",sans-serif;font-weight:700;font-size:44px;color:var(--white);letter-spacing:1px}
.hero-sub{left:0;top:388px;width:1200px;text-align:center;font-size:16px;color:var(--white)}
.arrow{top:368px}

/* weather */
.weather-title{left:98px;top:578px;font-family:"Montserrat",sans-serif;font-weight:700;font-size:22px;line-height:34px;color:var(--white)}
.vline{width:1px;background:rgba(255,255,255,.6)}
.w-text{font-size:15px;line-height:26px;color:var(--white);font-weight:600}
.temp{font-family:"Montserrat",sans-serif;font-weight:600;color:var(--white)}

/* calendar */
.cal-stack{left:104px;top:820px;width:364px;height:362px;background:#ddd;border:1px solid #ccc}
.calendar{left:98px;top:804px;width:368px;height:368px;background:var(--white);border:1px solid #ccc;box-shadow:0 3px 6px rgba(0,0,0,.2)}
.cal-head{height:56px;background:var(--green);color:var(--white);font-family:"Montserrat",sans-serif;font-weight:600;font-size:20px;text-align:center;line-height:56px;position:relative}
.cal-head .chev{position:absolute;top:0;font-size:26px;font-weight:700}
.cal-days{display:grid;grid-template-columns:repeat(7,1fr);font-size:11px;color:#555;text-align:center;padding:12px 0 6px}
.cal-grid{display:grid;grid-template-columns:repeat(7,1fr);grid-auto-rows:51px;border-top:1px solid #ddd}
.cal-grid span{display:flex;align-items:center;justify-content:center;font-size:14px;font-weight:700;color:#333;border-right:1px solid #e2e2e2;border-bottom:1px solid #e2e2e2;background:#f6f6f6}
.cal-grid span.out{color:#999;font-weight:400;background:var(--white)}
.cal-grid span.today{background:var(--green);color:var(--white)}

/* welcome */
.section-title{font-family:"Montserrat",sans-serif;font-weight:700;font-size:26px;color:var(--title-olive)}
.rule{height:2px;background:var(--title-olive)}
.welcome-sub{left:542px;top:876px;font-size:20px;font-weight:600;color:#444}
.bullet{left:542px;width:560px;display:flex;gap:14px;font-family:"Raleway",sans-serif;font-size:12px;line-height:20px;color:#666}
.bullet i{flex:0 0 16px;height:16px;border-radius:50%;border:2px solid var(--green);margin-top:2px;position:relative}
.bullet i::after{content:"";position:absolute;left:3px;top:3px;width:5px;height:5px;border-top:2px solid var(--green);border-right:2px solid var(--green);transform:rotate(45deg)}
.btn{display:flex;align-items:center;justify-content:center;color:var(--white);font-size:15px;font-weight:600}
.btn.green{background:var(--green)}
.btn.olive{background:var(--olive)}

/* rise and set */
.night-title{left:0;top:1332px;width:1200px;text-align:center;font-family:"Montserrat",sans-serif;font-weight:600;font-size:26px;color:var(--white)}
.tile{top:1462px;height:196px;background:var(--box-bottom);border:2px solid #7fa6dc;color:var(--white);text-align:center}
.tile .cap{height:56px;background:var(--box-top);font-size:13px;line-height:17px;display:flex;align-items:center;justify-content:center;padding:0 6px}
.tile .icon{margin:18px auto 6px;display:block}
.tile .val{font-size:20px;font-weight:600}

/* places */
.place-img{top:1988px;width:302px;height:192px;border-radius:18px 18px 44px 44px / 18px 18px 24px 24px}
.place-temp{top:2074px;display:flex;align-items:center;gap:12px;color:var(--white)}
.place-name{top:2214px;width:302px;text-align:center;font-family:"Montserrat",sans-serif;font-weight:700;font-size:19px}
.place-text{top:2250px;width:302px;text-align:center;font-family:"Raleway",sans-serif;font-size:12px;line-height:20px;color:#444}

/* footer */
.foot-brand{left:0;top:2540px;width:1200px;text-align:center;font-size:36px;font-weight:700;color:var(--white)}
.foot-brand .dot{display:inline-block;width:22px;height:22px;border:2px solid var(--white);border-radius:50%;vertical-align:middle;margin-right:10px}
.moon-title{left:0;top:2656px;width:1200px;text-align:center;font-family:"Montserrat",sans-serif;font-weight:700;font-size:22px;color:var(--white)}
.field-label{top:2724px;font-size:14px;color:var(--white)}
.select{top:2758px;height:46px;background:var(--white);font-size:14px;color:#333;padding:0 12px;display:flex;align-items:center;justify-content:space-between}
.select::after{content:"";border:6px solid transparent;border-top:7px solid #333;margin-top:6px}
.moon-btn{left:856px;top:2758px;width:232px;height:46px;background:var(--green);border:2px solid #c7e3a8;font-size:15px}
.foot-links{left:0;top:2860px;width:1200px;text-align:center;font-size:13px;font-weight:700;color:var(--white);word-spacing:2px}
.foot-links b{font-weight:400;margin:0 22px}
.foot-line{left:98px;top:2914px;width:990px;height:1px;background:rgba(255,255,255,.5)}
.copyright{left:98px;top:2940px;font-size:14px;color:var(--white)}
.social{top:2932px;width:34px;height:34px;border:2px solid var(--white);border-radius:50%}
</style>
</head>
<body>

<!-- header -->
<div class="abs brand"><span class="dot"></span>ZAWIRA</div>
<span class="abs main-nav" style="left:762px">KYNOLOGIA</span>
<span class="abs main-nav" style="left:906px">NOWOSCI</span>
<span class="abs main-nav" style="left:1038px">GALERIA</span>

<nav class="abs sub-nav">
  <span style="left:98px">Historia Kola</span>
  <span style="left:222px">Zarzad Kola</span>
  <span style="left:324px">Sklad Zarzadu</span>
  <span style="left:474px">Uchwaly i Regulaminy</span>
  <span style="left:634px">Urzadzenia Lowiecka</span>
  <span style="left:804px">Plan Polowan</span>
  <span style="left:976px">Kalendarz Polowan</span>
</nav>

<!-- hero -->
<div class="abs hero" role="img" aria-label="Sunlit forest with tall trees and green undergrowth"></div>
<h1 class="abs hero-title">ZAWIRA-DOLNOMOKRA</h1>
<p class="abs hero-sub">We are a hunting club located in Poland, called "ZAWIRA". The club was founded in 1945.</p>
<svg class="abs arrow" style="left:32px" width="30" height="56" viewBox="0 0 30 56"><path d="M26 2 L4 28 L26 54" fill="none" stroke="#fff" stroke-width="2"/></svg>
<svg class="abs arrow" style="left:1138px" width="30" height="56" viewBox="0 0 30 56"><path d="M4 2 L26 28 L4 54" fill="none" stroke="#fff" stroke-width="2"/></svg>

<!-- weather band -->
<svg class="abs" style="left:0;top:554px" width="1200" height="170" viewBox="0 0 1200 170">
  <defs><linearGradient id="band" x1="0" y1="0" x2="0" y2="1"><stop offset="0" stop-color="#4a9410"/><stop offset="1" stop-color="#5fae14"/></linearGradient></defs>
  <path d="M0 0 H1200 V96 Q600 210 0 96 Z" fill="url(#band)"/>
</svg>
<div class="abs weather-title">WEATHER CONDITION<br>OF POLAND</div>
<div class="abs vline" style="left:386px;top:586px;height:80px"></div>
<svg class="abs" style="left:420px;top:592px" width="40" height="40" viewBox="0 0 40 40"><circle cx="20" cy="20" r="19" fill="#fff"/><circle cx="20" cy="20" r="7" fill="none" stroke="#4f9a0c" stroke-width="3"/><g stroke="#4f9a0c" stroke-width="2.5"><path d="M20 6v5M20 29v5M6 20h5M29 20h5M10 10l3 3M27 27l3 3M30 10l-3 3M13 27l-3 3"/></g></svg>
<div class="abs temp" style="left:474px;top:584px;font-size:40px">29°</div>
<div class="abs temp" style="left:550px;top:584px;font-size:16px">°C | °F</div>
<div class="abs vline" style="left:642px;top:586px;height:80px"></div>
<div class="abs w-text" style="left:680px;top:592px">Warsaw, Poland<br>Friday 2:00 PM, Sunny</div>
<div class="abs vline" style="left:890px;top:586px;height:80px"></div>
<div class="abs w-text" style="left:920px;top:590px;line-height:23px">Precipitation: 0%<br>Humidity: 37%<br>Wind: 11km/h</div>

<!-- calendar -->
<div class="abs cal-stack"></div>
<section class="abs calendar">
  <div class="cal-head"><span class="chev" style="left:18px">‹</span>July 16 2017<span class="chev" style="right:18px">›</span></div>
  <div class="cal-days"><span>MON</span><span>TUE</span><span>WED</span><span>THU</span><span>FRI</span><span>SAT</span><span>SUN</span></div>
  <div class="cal-grid">
    <span class="out">30</span><span>1</span><span>2</span><span>3</span><span>4</span><span>5</span><span>6</span>
    <span>7</span><span>8</span><span>9</span><span>10</span><span>11</span><span>12</span><span>13</span>
    <span>14</span><span>15</span><span class="today">16</span><span>17</span><span>18</span><span>19</span><span>20</span>
    <span>21</span><span>22</span><span>23</span><span>24</span><span>25</span><span>26</span><span>27</span>
    <span>28</span><span>29</span><span>30</span><span>31</span><span class="out">1</span><span class="out">2</span><span class="out">3</span>
  </div>
</section>

<!-- welcome -->
<h2 class="abs section-title" style="left:542px;top:798px">WELCOME TO ZAWIRA</h2>
<div class="abs rule" style="left:542px;top:842px;width:178px"></div>
<p class="abs welcome-sub">Nemo enim ipsam voluptatem quia voluptas</p>
<div class="abs bullet" style="top:928px"><i></i><p>Nemo enim ipsam voluptatem quia voluptas sit aspernatur aut odit aut fugit, sed quia conse quuntur magni dolores eos qui ratione voluptatem sequi.</p></div>
<div class="abs bullet" style="top:990px"><i></i><p>Nemo enim ipsam voluptatem quia voluptas sit aspernatur aut odit aut fugit, sed quia conse quuntur magni dolores eos qui ratione voluptatem sequi.</p></div>
<div class="abs bullet" style="top:1052px"><i></i><p>Nemo enim ipsam voluptatem quia voluptas sit aspernatur aut odit aut fugit, sed quia conse quuntur magni dolores eos qui ratione voluptatem sequi.</p></div>
<div class="abs btn green" style="left:542px;top:1120px;width:140px;height:50px">Read More</div>

<!-- rise and set -->
<svg class="abs" style="left:0;top:1256px" width="1200" height="560" viewBox="0 0 1200 560" role="img" aria-label="Night sky with scattered stars">
  <defs><radialGradient id="night" cx="0.5" cy="0.5" r="0.7"><stop offset="0" stop-color="#1c2e5a"/><stop offset="1" stop-color="#08112a"/></radialGradient></defs>
  <path d="M0 60 Q600 -50 1200 60 V480 Q600 610 0 480 Z" fill="url(#night)"/>
</svg>
<h2 class="abs night-title">RISE AND SET TIME</h2>
<div class="abs" style="left:566px;top:1392px;width:70px;height:2px;background:#fff"></div>

<div class="abs tile" style="left:100px;width:202px">
  <div class="cap" style="font-size:15px">LOCAL WEATHER</div>
  <div style="display:flex;align-items:center;justify-content:center;gap:8px;margin-top:26px">
    <span style="font-size:58px;font-family:'Open Sans',sans-serif;line-height:1">16°</span>
    <svg width="80" height="60" viewBox="0 0 80 60"><g fill="none" stroke="#fff" stroke-width="3"><circle cx="30" cy="26" r="12"/><path d="M30 4v6M30 42v4M8 26h6M12 10l4 4M48 10l-4 4M12 42l4-4"/><path d="M34 52h36a10 10 0 0 0 0-20 14 14 0 0 0-26-2 10 10 0 0 0-10 22z" fill="#1d4f96"/></g></svg>
  </div>
</div>
<div class="abs tile" style="left:314px;width:140px">
  <div class="cap">Actual phase of the moon</div>
  <svg class="icon" width="40" height="40" viewBox="0 0 40 40"><circle cx="20" cy="20" r="18" fill="#fff"/><circle cx="14" cy="14" r="3" fill="#1d4f96"/><circle cx="25" cy="24" r="4" fill="#1d4f96"/><circle cx="14" cy="27" r="2" fill="#1d4f96"/></svg>
  <div style="font-size:15px;font-weight:700;line-height:20px">FULL MOON<br>PHASE</div>
</div>
<div class="abs tile" style="left:466px;width:140px">
  <div class="cap">Actual moon rising hour</div>
  <svg class="icon" width="44" height="40" viewBox="0 0 44 40"><path d="M18 6a12 12 0 1 0 12 16 10 10 0 0 1-12-16z" fill="#fff"/><path d="M16 36h20a7 7 0 0 0 0-14 9 9 0 0 0-16 2 6 6 0 0 0-4 12z" fill="#fff" stroke="#1d4f96" stroke-width="2"/></svg>
  <div class="val" style="margin-top:20px">10:20:30</div>
</div>
<div class="abs tile" style="left:614px;width:140px">
  <div class="cap">Actual moon set hour</div>
  <svg class="icon" width="40" height="40" viewBox="0 0 40 40"><path d="M22 4a16 16 0 1 0 14 22 13 13 0 0 1-14-22z" fill="#fff"/><path d="M28 10l2 5 5 .5-4 3 1.5 5-4.5-3-4.5 3 1.5-5-4-3 5-.5z" fill="#fff"/></svg>
  <div class="val" style="margin-top:20px">12:05:30</div>
</div>
<div class="abs tile" style="left:764px;width:140px">
  <div class="cap">Actual sun rise hour</div>
  <svg class="icon" width="48" height="40" viewBox="0 0 48 40"><path d="M10 30a14 14 0 0 1 28 0z" fill="#fff"/><g stroke="#fff" stroke-width="3"><path d="M24 4v8M6 14l6 5M42 14l-6 5M2 36h44"/></g></svg>
  <div class="val" style="margin-top:20px">08:11:30</div>
</div>
<div class="abs tile" style="left:916px;width:140px">
  <div class="cap">Actual sun set hour</div>
  <svg class="icon" width="48" height="40" viewBox="0 0 48 40"><g fill="none" stroke="#fff" stroke-width="3"><path d="M12 26a12 12 0 0 1 24 0"/><path d="M24 2v6M8 12l4 4M40 12l-4 4M2 30h44M8 36q4-3 8 0t8 0 8 0 8 0"/></g></svg>
  <div class="val" style="margin-top:20px">09:20:30</div>
</div>

<!-- hunting places -->
<h2 class="abs section-title" style="left:0;top:1876px;width:1200px;text-align:center">HUNTING PLACES</h2>
<div class="abs rule" style="left:560px;top:1932px;width:82px"></div>

<div class="abs place-img" style="left:118px;background:linear-gradient(180deg,#4e6a2a,#2f4a1c 70%,#3c5a26)" role="img" aria-label="Misty forest with a stream"></div>
<div class="abs place-img" style="left:452px;background:linear-gradient(180deg,#6a9a22,#4f8a18 60%,#7aa83a)" role="img" aria-label="Green rolling meadow at sunrise"></div>
<div class="abs place-img" style="left:784px;background:linear-gradient(180deg,#5e6a40,#4a5430 55%,#7a8050)" role="img" aria-label="Lake surrounded by trees"></div>

<div class="abs place-temp" style="left:176px">
  <svg width="36" height="36" viewBox="0 0 40 40"><circle cx="20" cy="20" r="19" fill="#fff"/><circle cx="20" cy="20" r="7" fill="none" stroke="#4f9a0c" stroke-width="3"/></svg>
  <span class="temp" style="font-size:40px">29°</span><span class="temp" style="font-size:15px;margin-top:-22px">°C | °F</span>
</div>
<div class="abs place-temp" style="left:510px">
  <svg width="36" height="36" viewBox="0 0 40 40"><circle cx="20" cy="20" r="19" fill="#fff"/><circle cx="20" cy="20" r="7" fill="none" stroke="#4f9a0c" stroke-width="3"/></svg>
  <span class="temp" style="font-size:40px">15°</span><span class="temp" style="font-size:15px;margin-top:-22px">°C | °F</span>
</div>
<div class="abs place-temp" style="left:842px">
  <svg width="36" height="36" viewBox="0 0 40 40"><circle cx="20" cy="20" r="19" fill="#fff"/><circle cx="20" cy="20" r="7" fill="none" stroke="#4f9a0c" stroke-width="3"/></svg>
  <span class="temp" style="font-size:40px">30°</span><span class="temp" style="font-size:15px;margin-top:-22px">°C | °F</span>
</div>

<h3 class="abs place-name" style="left:118px;color:var(--title-olive)">Nemo enim ipsam</h3>
<h3 class="abs place-name" style="left:452px;color:var(--green)">Excepteur sint occaecat</h3>
<h3 class="abs place-name" style="left:784px;color:var(--title-olive)">Duis aute irure</h3>
<p class="abs place-text" style="left:118px">Nemo enim ipsam voluptatem quia voluptas sit aspernatur aut odit aut fugit, sed quia consequun tur magni dolores eos qui.</p>
<p class="abs place-text" style="left:452px">Nemo enim ipsam voluptatem quia voluptas sit aspernatur aut odit aut fugit, sed quia consequun tur magni dolores eos qui.</p>
<p class="abs place-text" style="left:784px">Nemo enim ipsam voluptatem quia voluptas sit aspernatur aut odit aut fugit, sed quia consequun tur magni dolores eos qui.</p>
<div class="abs btn olive" style="left:211px;top:2334px;width:116px;height:42px;font-size:14px">Read More</div>
<div class="abs btn green" style="left:545px;top:2334px;width:116px;height:42px;font-size:14px">Read More</div>
<div class="abs btn olive" style="left:877px;top:2334px;width:116px;height:42px;font-size:14px">Read More</div>

<!-- footer -->
<svg class="abs" style="left:0;top:2466px" width="1200" height="534" viewBox="0 0 1200 534">
  <path d="M0 70 Q600 -60 1200 70 V534 H0 Z" fill="#3d3c1a"/>
</svg>
<div class="abs foot-brand"><span class="dot"></span>ZAWIRA</div>
<h2 class="abs moon-title">FAZY KSIEZYCA</h2>
<span class="abs field-label" style="left:110px">Rok:</span>
<span class="abs field-label" style="left:360px">Miesiac:</span>
<span class="abs field-label" style="left:606px">Dzien:</span>
<div class="abs select" style="left:110px;width:234px">2014</div>
<div class="abs select" style="left:362px;width:230px">Email</div>
<div class="abs select" style="left:606px;width:232px">Email</div>
<div class="abs btn moon-btn">POKAZ FAZY KSIEZYCA</div>
<div class="abs foot-links">HISTORIA KOLA<b>|</b>ZARZAD KOLA<b>|</b>SKLAD ZARZADU<b>|</b>UCHWALY I REGULAMINY<b>|</b>URZADZENIA LOWIECKA<b>|</b>PLAN POLOWAN</div>
<div class="abs foot-line"></div>
<p class="abs copyright">© Copyright 2017 zawira. All Right Reserved</p>
<span class="abs social" style="left:878px" aria-label="Social link"></span>
<span class="abs social" style="left:924px" aria-label="Social link"></span>
<span class="abs social" style="left:970px" aria-label="Social link"></span>
<span class="abs social" style="left:1016px" aria-label="Social link"></span>
<span class="abs social" style="left:1062px" aria-label="Social link"></span>

</body>
</html>
```